ROVA NET LTD

Advertisement to get more schools:
use website https://www.rova-net.co.uk for logos etc.
ICT Service Level Agreements for as little as £2000 per year
Unlimited Remote, phone and email support
Unlimited Call outs included
90% fix time within 30 minutes of ticket submission
Extra support during Brelcom inspections
GDPR service included

Education

```html
<!DOCTYPE html>
<html lang="en">
<head>
<meta charset="utf-8">
<title>ROVA NET – ICT SLA Agreements</title>
<link rel="stylesheet" href="https://fonts.googleapis.com/css2?family=Montserrat:wght@300;400;600;700;800;900&family=Oswald:wght@700&display=swap">
<style>
:root{
  --page-bg:#e2e2e2;
  --paper:#ffffff;
  --blue:#0f63a6;
  --orange:#f2814a;
  --ink:#222222;
  --footer:#222222;
  --white:#ffffff;
}
*{box-sizing:border-box;margin:0;padding:0}
html,body{width:1200px;height:1200px;overflow:hidden;background:var(--page-bg);font-family:'Montserrat',sans-serif}
.flyer{position:absolute;left:271px;top:53px;width:660px;height:1093px;background:var(--paper);box-shadow:0 4px 18px rgba(0,0,0,.18);overflow:hidden}
.brand{position:absolute;left:0;right:0;top:46px;text-align:center}
.brand-name{display:inline-flex;align-items:center;gap:10px;font-weight:800;font-size:44px;color:var(--blue);letter-spacing:1px;line-height:1}
.brand-name .mark{width:30px;height:30px;background:var(--orange);border-radius:4px}
.brand-tag{margin-top:14px;font-weight:600;font-size:12.5px;color:var(--blue);letter-spacing:1px}
.accent{position:absolute;background:var(--orange)}
.accent.top{left:0;top:145px;width:206px;height:7px;clip-path:polygon(0 0,97% 0,100% 100%,0 100%)}
.accent.mid{left:443px;top:480px;width:217px;height:7px;clip-path:polygon(3% 0,100% 0,100% 100%,0 100%)}
.accent.foot{left:188px;top:951px;width:284px;height:9px}
.hero{position:absolute;left:0;top:157px;width:660px;height:318px;background:var(--blue);overflow:hidden}
.hero-art{position:absolute;right:0;top:0;width:370px;height:318px;background:radial-gradient(circle at 62% 48%,#6fc3f5 0%,#2a7fc4 28%,#0d4f8c 62%,transparent 100%),linear-gradient(90deg,var(--blue),#0b4c86)}
.hero-copy{position:absolute;left:36px;top:35px;color:var(--white);line-height:1}
.hero-copy .get{font-weight:400;font-size:41px}
.hero-copy .sla{font-weight:900;font-size:70px;color:var(--orange);letter-spacing:-3px;margin-top:10px}
.hero-copy .line{font-weight:800;font-size:40px;letter-spacing:-2px;margin-top:6px}
.hero-copy .under{width:52px;height:3px;background:var(--orange);margin:8px 0 12px}
.hero-copy .price{display:flex;align-items:center;gap:12px}
.price .as{font-weight:300;font-size:42px}
.price .amount{font-weight:900;font-size:48px;color:var(--orange);letter-spacing:-1px}
.price .per{font-weight:800;font-size:16px;line-height:1}
.features{position:absolute;top:534px;left:38px;right:38px;display:flex;justify-content:space-between}
.feature{position:relative;width:188px;height:90px;background:var(--orange);border-radius:16px;padding:6px}
.feature-inner{height:100%;border:2px dashed rgba(255,255,255,.85);border-radius:12px;display:flex;align-items:flex-end;justify-content:center;padding-bottom:10px;text-align:center;color:var(--white);font-weight:700;font-size:16px;line-height:1.05}
.feature-icon{position:absolute;left:50%;top:-23px;transform:translateX(-50%);width:52px;height:52px;border-radius:50%;background:var(--white);border:4px solid var(--blue);display:flex;align-items:center;justify-content:center}
.stat{position:absolute;top:642px;left:88px;display:flex;align-items:center;gap:18px}
.stat-value{font-family:'Oswald',sans-serif;font-weight:700;font-size:64px;color:var(--orange);letter-spacing:-2px}
.stat-text{font-weight:600;font-size:25px;line-height:1.3;color:var(--ink);letter-spacing:.5px}
.benefit{position:absolute;top:756px;width:242px;height:163px;box-shadow:0 6px 18px rgba(0,0,0,.15);border:3px solid var(--white)}
.benefit.left{left:57px}
.benefit.right{left:359px}
.benefit-photo{position:absolute;inset:0}
.benefit.left .benefit-photo{background:linear-gradient(135deg,#e6b96b 0%,#b06aa8 40%,#5a4c7a 75%,#2c3650 100%)}
.benefit.right .benefit-photo{background:linear-gradient(135deg,#4a6fa0 0%,#8aa4cc 45%,#3a4c86 80%,#243060 100%)}
.benefit-caption{position:absolute;left:0;right:0;bottom:0;height:54px;background:rgba(70,70,80,.62);color:var(--white);font-weight:600;font-size:17px;line-height:1.2;display:flex;align-items:center;justify-content:center;text-align:center}
.footer{position:absolute;left:0;top:955px;width:660px;height:138px;background:var(--footer)}
.contacts{position:absolute;left:57px;top:31px;list-style:none}
.contacts li{display:flex;align-items:center;gap:12px;color:var(--white);font-weight:600;font-size:16px;height:24px}
.contacts svg{width:18px;height:18px}
.divider{position:absolute;left:338px;top:29px;height:79px;border-left:1px dashed #777}
.follow{position:absolute;left:428px;top:79px;display:flex;align-items:center;gap:6px;color:var(--orange);font-weight:700;font-size:15px}
.follow .dot{width:20px;height:20px;border-radius:50%;border:1.5px solid #aaa}
.follow .label{margin-right:2px}
</style>
</head>
<body>
<main class="flyer">
  <header class="brand">
    <div class="brand-name"><span class="mark"></span>ROVA NET</div>
    <div class="brand-tag">SCHOOL IT SERVICES &amp; SUPPORT</div>
  </header>

  <div class="accent top"></div>

  <section class="hero">
    <div class="hero-art" role="img" aria-label="Glowing blue circuit board chip labelled ICT with a hand touching it"></div>
    <div class="hero-copy">
      <div class="get">GET</div>
      <div class="sla">ICT SLA</div>
      <div class="line">AGREEMENTS</div>
      <div class="line">FOR AS LITTLE</div>
      <div class="under"></div>
      <div class="price"><span class="as">AS</span><span class="amount">£2000</span><span class="per">PER<br>YEAR</span></div>
    </div>
  </section>

  <div class="accent mid"></div>

  <section class="features">
    <div class="feature">
      <div class="feature-icon">
        <svg width="26" height="26" viewBox="0 0 26 26"><rect x="5" y="9" width="16" height="9" rx="3" transform="rotate(-35 13 13)" fill="#444"/><path d="M17 4a5 5 0 0 1 5 5M17 7a2 2 0 0 1 2 2" stroke="#444" stroke-width="1.5" fill="none"/></svg>
      </div>
      <div class="feature-inner">Unlimited<br>Remote</div>
    </div>
    <div class="feature">
      <div class="feature-icon">
        <svg width="26" height="26" viewBox="0 0 26 26"><rect x="3" y="7" width="17" height="12" fill="none" stroke="#444" stroke-width="1.8"/><path d="M3 7l8.5 7L20 7" fill="none" stroke="#444" stroke-width="1.8"/><circle cx="20" cy="19" r="4.5" fill="#444"/></svg>
      </div>
      <div class="feature-inner">Phone and<br>email support</div>
    </div>
    <div class="feature">
      <div class="feature-icon">
        <svg width="26" height="26" viewBox="0 0 26 26"><path d="M7 4l3 4-2 2c1 3 3 5 6 6l2-2 4 3-2 3C11 20 5 14 4 7z" fill="#444"/><path d="M15 5a6 6 0 0 1 6 6M15 8a3 3 0 0 1 3 3" stroke="#444" stroke-width="1.5" fill="none"/></svg>
      </div>
      <div class="feature-inner">Unlimited Call<br>outs included</div>
    </div>
  </section>

  <section class="stat">
    <div class="stat-value">90%</div>
    <div class="stat-text">fix time within 30 minutes<br>of ticket submission</div>
  </section>

  <figure class="benefit left">
    <div class="benefit-photo" role="img" aria-label="Teacher with young pupils looking at a tablet in a classroom"></div>
    <figcaption class="benefit-caption">Extra support during<br>Brelcom inspections</figcaption>
  </figure>
  <figure class="benefit right">
    <div class="benefit-photo" role="img" aria-label="Child using a laptop surrounded by glowing digital data"></div>
    <figcaption class="benefit-caption">GDPR service<br>included</figcaption>
  </figure>

  <div class="accent foot"></div>

  <footer class="footer">
    <ul class="contacts">
      <li><svg viewBox="0 0 18 18"><path d="M4 1l3 4-2 2c1 3 3 5 6 6l2-2 4 3-2 3C7 17 1 11 1 4z" fill="#f2814a"/></svg>0161 555 0142</li>
      <li><svg viewBox="0 0 18 18"><rect x="1" y="4" width="16" height="11" fill="#f2814a"/><path d="M1 4l8 6 8-6" fill="none" stroke="#222" stroke-width="1.4"/></svg>info@rova-net.co.uk</li>
      <li><svg viewBox="0 0 18 18"><circle cx="9" cy="9" r="7.5" fill="none" stroke="#f2814a" stroke-width="1.6"/><ellipse cx="9" cy="9" rx="3.2" ry="7.5" fill="none" stroke="#f2814a" stroke-width="1.4"/><path d="M1.5 9h15M3 5h12M3 13h12" stroke="#f2814a" stroke-width="1.2"/></svg>www.rova-net.co.uk</li>
    </ul>
    <div class="divider"></div>
    <div class="follow"><span class="label">FOLLOW US</span><span class="dot"></span><span class="dot"></span><span class="dot"></span></div>
  </footer>
</main>
</body>
</html>
```